World renowned cocktail bar needs a "free cocktail" voucher

I need a "FREE COCKTAIL" voucher for a partnership with a local real estate agent. The flyer needs to be DL and singles sided.

About us:
We are a unique and fun 1950’s style bar - a relaxed local meeting place, the kind of bar where your bartender drinks on their night off. The final design should be playful and reflect the fun feeling of the bar along with the enthusiastic spirit of the 1950s cocktail culture. For more of an idea of what we are about please see our website- wobblyjigs.com.au

About the flyer:
This flyer is to welcome people into the area and offer them a free cocktail. It needs to have the text below along with the Wobbly Jigs logo and the TR Prewitt logo (both attached) somewhere on the flyer but not too large. The Wobbly Jigs logo should be more prominent. Please also include the address: 472 Quillmore rd (just opposite the fire station), the phone number- 8152 4907 and the website- wobblyjigs.com.au

The text:
Welcome to the neighbourhood! Wobbly Jigs is a world famous cocktail bar, your new local and a well kept secret. Now you've moved into such a great suburb we would love to buy you a drink and introduce ourselves.
Come and say hi. We'd love to help you get to know the area.

```html
<!DOCTYPE html>
<html lang="en">
<head>
<meta charset="utf-8">
<title>Wobbly Jigs – Free Cocktail Voucher</title>
<link rel="stylesheet" href="https://fonts.googleapis.com/css2?family=Oswald:wght@400;500;600;700&family=Abel&family=Poiret+One&display=swap">
<style>
  :root{
    --backdrop:#e9e5de;
    --peach:#fbd8a0;
    --peach-light:#fde7c0;
    --peach-pale:#fff1d8;
    --teal:#3aa7c6;
    --lime:#e5dc5f;
    --red:#e32b3a;
    --ink:#1e1a1a;
    --cream:#fff7ea;
    --orange:#f3a94a;
  }
  *{box-sizing:border-box;margin:0;padding:0}
  html,body{width:1200px;height:1000px;overflow:hidden;background:var(--backdrop)}
  .voucher{position:absolute;left:356px;top:48px;width:450px;height:897px;background:var(--peach);overflow:hidden;box-shadow:0 6px 18px rgba(0,0,0,.18)}
  .voucher-shapes{position:absolute;inset:0}
  .brand-name{position:absolute;left:26px;top:92px;width:210px;font-family:"Oswald",sans-serif;font-weight:700;font-size:52px;line-height:.95;color:var(--ink);transform:rotate(-8deg);text-transform:uppercase}
  .offer{position:absolute;left:250px;top:40px;width:170px;transform:rotate(-16deg);font-family:"Poiret One",sans-serif;color:var(--red);text-align:center;font-weight:400;line-height:.95}
  .offer span{display:block}
  .offer .free{font-size:52px}
  .offer .cocktail{font-size:40px}
  .glass-art{position:absolute;left:310px;top:190px;width:100px;height:90px;border-radius:50% 50% 8px 8px;background:linear-gradient(160deg,#f6f3d6,#c9dfb0)}
  .welcome{position:absolute;left:50px;top:250px;width:340px;text-align:center;transform:rotate(-12deg);color:var(--cream)}
  .welcome-title{font-family:"Poiret One",sans-serif;font-size:34px;letter-spacing:8px;color:var(--orange);font-weight:400;line-height:1}
  .welcome-sub{font-family:"Oswald",sans-serif;font-weight:600;font-size:21px;color:var(--orange);margin-bottom:8px}
  .welcome-body{font-family:"Abel",sans-serif;font-size:16.5px;line-height:1.35}
  .welcome-cta{font-family:"Oswald",sans-serif;font-weight:500;font-size:24px;margin:6px 0 4px;text-transform:uppercase}
  .welcome-note{font-family:"Abel",sans-serif;font-size:16px}
  .couple-art{position:absolute;left:180px;top:520px;width:270px;height:210px;background:linear-gradient(180deg,#4fb2cf 0%,#2f8fab 60%,#1f2a33 100%)}
  .partner{position:absolute;left:16px;top:602px;width:160px;font-family:"Oswald",sans-serif;color:var(--ink)}
  .partner-name{display:flex;align-items:center;gap:6px;font-weight:600;font-size:20px;line-height:1}
  .partner-name::before{content:"";width:16px;height:16px;background:var(--ink)}
  .partner-branch{font-weight:600;font-size:16px;margin-top:6px;padding-left:8px}
  .partner-service{font-weight:500;font-size:11px;line-height:1.2;padding-left:14px}
  .contact{position:absolute;left:60px;top:752px;width:370px;font-family:"Oswald",sans-serif;color:var(--ink);text-align:center}
  .contact-address{font-size:21px;font-weight:500;letter-spacing:1px}
  .contact-landmark{font-size:13px;letter-spacing:1.2px;margin-top:2px;text-transform:uppercase}
  .contact-phone{font-size:27px;font-weight:600;letter-spacing:3px;margin-top:8px;text-align:left;padding-left:8px}
  .contact-web{font-size:25px;font-weight:600;letter-spacing:3px;text-align:left;padding-left:8px;text-transform:uppercase}
</style>
</head>
<body>
<main class="voucher">
  <svg class="voucher-shapes" width="450" height="897" viewBox="0 0 450 897">
    <circle cx="95" cy="85" r="140" fill="var(--peach-light)"/>
    <circle cx="95" cy="85" r="95" fill="var(--peach-pale)"/>
    <polygon points="0,272 450,168 450,730 112,730" fill="var(--teal)"/>
    <polygon points="236,52 400,8 450,180 290,225" fill="var(--lime)"/>
    <polygon points="0,740 18,738 48,897 0,897" fill="var(--peach-light)"/>
    <polygon points="6,742 450,726 450,897 38,897" fill="#3a2e28"/>
    <polygon points="14,738 450,724 450,890 44,890" fill="var(--lime)"/>
  </svg>

  <h1 class="brand-name">Wobbly Jigs</h1>

  <div class="offer"><span class="free">FREE</span><span class="cocktail">COCKTAIL</span></div>
  <div class="glass-art" role="img" aria-label="Illustration of a martini glass with an olive"></div>

  <section class="welcome">
    <h2 class="welcome-title">WELCOME</h2>
    <p class="welcome-sub">to the neighbourhood!</p>
    <p class="welcome-body">Wobbly Jigs is a world famous cocktail bar, your new local and a well kept secret. Now you've moved into such a great suburb we would love to buy you a drink and introduce ourselves.</p>
    <p class="welcome-cta">Come and say hi.</p>
    <p class="welcome-note">We'd love to help you get to know the area.</p>
  </section>

  <div class="couple-art" role="img" aria-label="Retro illustration of a couple toasting with cocktails at a bar"></div>

  <div class="partner">
    <div class="partner-name">TR Prewitt</div>
    <div class="partner-branch">Inner City</div>
    <div class="partner-service">Property Investment<br>Management</div>
  </div>

  <address class="contact" style="font-style:normal">
    <div class="contact-address">472 Quillmore Rd Quillmore</div>
    <div class="contact-landmark">(Just opposite the fire station)</div>
    <div class="contact-phone">Phone: 8152 4907</div>
    <div class="contact-web">wobblyjigs.com.au</div>
  </address>
</main>
</body>
</html>
```